My Book needs a front and back cover design

I need you to design my front and back cover of my book. The title of my book is : Lanterns Past Harbour
Tide Notes
7 paths to gardening calmly always

The picture that I uploaded needs to be on the front cover. On the back cover it should be excerpt from Chapter One like this :

As years have gone by I have become much more conscious about my problem with stuttering, more able to relax my muscles to alleviate it. At the age of 20, I realized that stuttering is like a demon in my head that needs to be killed and that nothing is wrong with me. Furthermore, no one can help me but myself. I'm holding the key of my future. Everything is just in my head.

With this book, I want to help you realize that nobody can help you fix your stuttering better than yourself. There's no quick-get-rid-of-stuttering cure. The cure lies inside of you.

- Lorcan Vittel, excerpt from Chapter One
----------------------------------------------------------------------------------

My name also needs to be located on the front cover.

Target Market(s)

80 million people who stutter each day

Industry/Entity Type

Psychology

Font styles to use
Serif
Sans Serif

Colors
1b1b1b
000000
333333

Requirements
Must have
• Front Cover : Full Title and subtitle and my name and my picture
• Back Cover : Excerpt from my Chapter One with my name below just as I have described in my project description
Nice to have
• Maybe black background would be the best for the front cover.

```html
<!DOCTYPE html>
<html lang="en">
<head>
<meta charset="utf-8">
<title>Lanterns Past Harbour – Cover Layouts</title>
<link rel="stylesheet" href="https://fonts.googleapis.com/css2?family=Cinzel:wght@400&family=Oswald:wght@500&family=Tinos:ital,wght@1,400;1,700&display=swap">
<style>
  :root {
    --backdrop: #1b1b1b;
    --cover-black: #000000;
    --cover-deep: #080808;
    --type-silver: #bdbdbd;
    --type-light: #d6d6d6;
    --type-dim: #8f8f8f;
    --band-dark: #b8962f;
    --band-light: #efd98a;
    --band-ink: #2a2108;
    --photo-glow: #333333;
  }
  * { margin: 0; padding: 0; box-sizing: border-box; }
  html, body { width: 1200px; height: 1200px; overflow: hidden; background: var(--backdrop); }
  .board { position: relative; width: 1200px; height: 1200px; }

  .cover {
    position: absolute;
    width: 686px; height: 506px;
    background: linear-gradient(180deg, var(--cover-black) 0%, var(--cover-deep) 100%);
    color: var(--type-silver);
    overflow: hidden;
  }
  .cover--plain { left: 220px; top: 90px; }
  .cover--banded { left: 218px; top: 616px; }

  .title-serif { font-family: "Cinzel", serif; font-weight: 400; line-height: 1; text-align: center; }
  .italic-serif { font-family: "Tinos", serif; font-style: italic; }
  .name-block { position: absolute; text-align: center; }
  .name { font-family: "Oswald", sans-serif; font-weight: 500; letter-spacing: 2px; color: var(--type-silver); line-height: 1; }
  .name-note { font-family: "Cinzel", serif; letter-spacing: 2px; color: var(--type-dim); line-height: 1; margin-top: 3px; }

  /* back cover */
  .back-title { position: absolute; left: 40px; width: 244px; top: 133px; font-size: 14px; letter-spacing: 1px; line-height: 1.1; }
  .back-excerpt { position: absolute; left: 42px; width: 240px; top: 197px; font-size: 8.6px; line-height: 11.7px; text-align: justify; text-align-last: center; color: var(--type-light); }
  .back-excerpt p + p { margin-top: 11px; }
  .back-name { left: 40px; width: 244px; top: 352px; }
  .back-name .name { font-size: 22px; }
  .back-name .name-note { font-size: 7px; letter-spacing: 1.6px; }

  /* spine */
  .spine { position: absolute; left: 324px; top: 186px; height: 310px; writing-mode: vertical-rl; display: flex; align-items: flex-start; gap: 18px; }
  .spine-name { display: flex; gap: 4px; }
  .spine-name .name { font-size: 18px; letter-spacing: 1.5px; }
  .spine-name .name-note { font-size: 5.6px; margin-top: 0; letter-spacing: 1.6px; }
  .spine-title { font-size: 17px; letter-spacing: 1px; line-height: 1.05; text-align: left; }

  /* front cover */
  .front-title { position: absolute; left: 384px; width: 290px; top: 48px; font-size: 33px; color: var(--type-silver); letter-spacing: 1px; }
  .front-title span { display: block; margin-bottom: 7px; }
  .front-subtitle { position: absolute; left: 384px; width: 290px; top: 133px; text-align: center; font-size: 14px; line-height: 18px; color: var(--type-silver); font-weight: 700; }
  .front-subtitle .series { letter-spacing: 1px; }
  .portrait {
    position: absolute; left: 418px; width: 210px; top: 196px; height: 310px;
    background: radial-gradient(ellipse 45% 60% at 50% 35%, var(--photo-glow) 0%, #141414 55%, transparent 100%);
  }
  .front-name { left: 384px; width: 290px; top: 454px; }
  .front-name .name { font-size: 29px; letter-spacing: 2.5px; }
  .front-name .name-note { font-size: 8.5px; letter-spacing: 2.6px; }

  /* gold band variant */
  .gold-band {
    position: absolute; left: 0; top: 124px; width: 100%; height: 49px;
    background: linear-gradient(90deg, var(--band-dark) 0%, var(--band-light) 35%, var(--band-dark) 55%, var(--band-light) 80%, var(--band-dark) 100%);
    border-top: 2px solid var(--band-light);
    border-bottom: 2px solid var(--band-light);
    box-shadow: 0 -3px 0 -1px var(--cover-black), 0 -4px 0 -1px var(--band-dark), 0 3px 0 -1px var(--cover-black), 0 4px 0 -1px var(--band-dark);
  }
  .cover--banded .back-title { color: var(--band-ink); top: 136px; }
  .cover--banded .front-subtitle { color: var(--band-ink); top: 134px; }
</style>
</head>
<body>
<main class="board">

  <section class="cover cover--plain" aria-label="Book jacket, black edition">
    <div class="back-title title-serif">Lanterns Past<br>Harbour</div>
    <div class="back-excerpt italic-serif">
      <p>As years have gone by I have become much more conscious about my problem with stuttering, more able to relax my muscles to alleviate it. At the age of 20, I realized that stuttering is like a demon in my head that needs to be killed and that nothing is wrong with me. Furthermore, no one can help me but myself. I'm holding the key of my future. Everything is just in my head.</p>
      <p>With this book, I want to help you realize that nobody can help you fix your stuttering better than yourself. There's no quick-get-rid-of-stuttering cure. The cure lies inside of you.</p>
    </div>
    <div class="name-block back-name"><div class="name">LORCAN VITTEL</div><div class="name-note">Excerpt from Chapter One</div></div>

    <div class="spine">
      <div class="spine-name"><div class="name">LORCAN VITTEL</div><div class="name-note">Excerpt from Chapter One</div></div>
      <div class="spine-title title-serif">Lanterns Past<br>Harbour</div>
    </div>

    <h1 class="front-title title-serif"><span>Lanterns</span><span>Past Harbour</span></h1>
    <div class="front-subtitle italic-serif"><div class="series">Tide Notes</div><div>7 paths to gardening calmly always</div></div>
    <div class="portrait" role="img" aria-label="Author portrait photograph: man in a black polo shirt against a dark background"></div>
    <div class="name-block front-name"><div class="name">LORCAN VITTEL</div><div class="name-note">Excerpt from Chapter One</div></div>
  </section>

  <section class="cover cover--banded" aria-label="Book jacket, gold band edition">
    <div class="gold-band"></div>
    <div class="back-title title-serif">Lanterns Past<br>Harbour</div>
    <div class="back-excerpt italic-serif" style="top:200px">
      <p>As years have gone by I have become much more conscious about my problem with stuttering, more able to relax my muscles to alleviate it. At the age of 20, I realized that stuttering is like a demon in my head that needs to be killed and that nothing is wrong with me. Furthermore, no one can help me but myself. I'm holding the key of my future. Everything is just in my head.</p>
      <p>With this book, I want to help you realize that nobody can help you fix your stuttering better than yourself. There's no quick-get-rid-of-stuttering cure. The cure lies inside of you.</p>
    </div>
    <div class="name-block back-name"><div class="name">LORCAN VITTEL</div><div class="name-note">Excerpt from Chapter One</div></div>

    <div class="spine">
      <div class="spine-name"><div class="name">LORCAN VITTEL</div><div class="name-note">Excerpt from Chapter One</div></div>
      <div class="spine-title title-serif">Lanterns Past<br>Harbour</div>
    </div>

    <h2 class="front-title title-serif"><span>Lanterns</span><span>Past Harbour</span></h2>
    <div class="front-subtitle italic-serif"><div class="series">Tide Notes</div><div>7 paths to gardening calmly always</div></div>
    <div class="portrait" role="img" aria-label="Author portrait photograph: man in a black polo shirt against a dark background"></div>
    <div class="name-block front-name"><div class="name">LORCAN VITTEL</div><div class="name-note">Excerpt from Chapter One</div></div>
  </section>

</main>
</body>
</html>
```